Business Card Design for new social media business

I am looking for a new professional business card design for an exciting new company which is based on providing members with experiences of others to benefit their choice of places to visit for restaurants, bars, clubs, national monument, tourist sights, hotels and so forth.
Updates

Please submit designs as I will choose to commit the funds depending on designs.

Target Market(s)

Business Managers as well as directors alongside owners

Industry/Entity Type

Business

Requirements
Must have
• Logo design and symbols
Nice to have
• Logo / Symbol on the back of the business card and possibly the logo as if embedded/embossed on the business card.

```html
<!DOCTYPE html>
<html lang="en">
<head>
<meta charset="utf-8">
<title>Vistaly business card – front and back</title>
<link rel="stylesheet" href="https://fonts.googleapis.com/css2?family=Tinos:ital,wght@0,400;0,700;1,400&family=Kalam&display=swap">
<style>
  :root {
    --paper: #ffffff;
    --ink: #000000;
    --brand-blue: #1f5cb8;
    --rule-blue: #1aa0dc;
    --rule-orange: #f0892a;
    --mark-orange: #f7941d;
  }
  * { margin: 0; padding: 0; box-sizing: border-box; }
  html, body {
    width: 1200px; height: 347px; overflow: hidden;
    background: var(--paper); color: var(--ink);
    font-family: "Tinos", "Times New Roman", serif;
  }
  .sheet { position: relative; width: 1200px; height: 347px; }
  .side-label { position: absolute; top: -2px; font-size: 14px; }
  .side-label--front { left: 16px; }
  .side-label--back { right: 16px; }

  .card {
    position: absolute; top: 17px; height: 314px;
    border: 2px solid var(--ink); background: var(--paper);
  }
  .card--front { left: 17px; width: 568px; }
  .card--back { left: 619px; width: 565px; }

  .brand { position: absolute; display: flex; align-items: center; color: var(--brand-blue); font-weight: 700; }
  .brand__dot { border-radius: 50%; background: var(--mark-orange); flex: none; }
  .card--front .brand { left: 30px; top: 62px; font-size: 38px; gap: 10px; }
  .card--front .brand__dot { width: 28px; height: 28px; }
  .card--back .brand { left: 50%; top: 50%; transform: translate(-50%, -50%); font-size: 92px; gap: 24px; }
  .card--back .brand__dot { width: 64px; height: 64px; }

  .tagline {
    position: absolute; left: 30px; top: 140px;
    font-family: "Kalam", cursive; font-size: 18px;
    transform: rotate(-3deg); transform-origin: left center;
  }

  .divider-vertical { position: absolute; left: 278px; top: 31px; width: 2px; height: 178px; background: var(--rule-blue); }
  .identity { position: absolute; left: 296px; top: 34px; }
  .identity__name { font-size: 23px; font-weight: 700; line-height: 1.2; }
  .identity__role { font-size: 23px; font-style: italic; line-height: 1.3; }

  .divider-horizontal { position: absolute; left: 22px; top: 220px; width: 526px; height: 2px; background: var(--rule-orange); }
  .contact {
    position: absolute; left: 0; right: 0; top: 229px;
    text-align: center; font-size: 15.5px; line-height: 21.5px;
  }
  .contact b { font-weight: 700; }
</style>
</head>
<body>
<div class="sheet">
  <span class="side-label side-label--front">front</span>
  <span class="side-label side-label--back">back</span>

  <section class="card card--front">
    <div class="brand"><span class="brand__dot"></span><span class="brand__name">Vistaly</span></div>
    <p class="tagline">More than meets the eye</p>
    <div class="divider-vertical"></div>
    <div class="identity">
      <p class="identity__name">Name Surname</p>
      <p class="identity__role">Specialty</p>
    </div>
    <div class="divider-horizontal"></div>
    <div class="contact">
      <p><b>Address:</b> 00, my adress str. | <b>Country:</b> Country | <b>P.O. Box:</b> 100 00</p>
      <p><b>Tel:</b> +88 100 00 00 000 | <b>Mob:</b> +88 000 00 00 000</p>
      <p><b>Email:</b> my email@example.com | <b>Website:</b> www.example.com</p>
    </div>
  </section>

  <section class="card card--back">
    <div class="brand"><span class="brand__dot"></span><span class="brand__name">Vistaly</span></div>
  </section>
</div>
</body>
</html>
```